We need a design for a contracting company website based in KSA, something modern with the same color theme as the attached logo. including a page for people who want to submit their CV and try to apply for a job.Also to include the "about us, contact us, gallery, Divisions, Supplies, etc...". If possible to have an interactive or moving background. Please disregard the "Keen Methods" Section in the attached profile.

Industry/Entity Type

Construction Company

Number of Pages Required

5+ page

Colors

Designer to choose colors to be used in the design.

Requirements
Must have
• Pages:
• about us, contact us, gallery, Divisions, Apply for a job, Supplies
Nice to have
• - Moving or interactive background

```html
<!DOCTYPE html>
<html lang="en">
<head>
<meta charset="utf-8">
<title>Cobaltrine Building Company</title>
<link href="https://fonts.googleapis.com/css2?family=Poppins:wght@300;400;500;600;700&display=swap" rel="stylesheet">
<style>
:root{
  --brown:#3b3028;
  --brown-deep:#2f2620;
  --brown-line:#54463b;
  --yellow:#f5ac1d;
  --yellow-soft:#f7b733;
  --white:#ffffff;
  --paper:#f4f4f4;
  --ink:#2c2520;
  --grey:#8a8580;
  --muted:#c9c0b6;
}
*{margin:0;padding:0;box-sizing:border-box}
html,body{width:1200px;height:4215px;overflow:hidden}
body{font-family:'Poppins',sans-serif;color:var(--ink);background:var(--white);position:relative}
section,header,footer{position:absolute;left:0;width:1200px}
.abs{position:absolute}

/* header */
.site-header{top:0;height:80px;background:var(--brown)}
.brand{left:84px;top:20px;display:flex;align-items:center;gap:10px}
.brand-mark{width:26px;height:26px;background:var(--yellow)}
.brand-name{color:var(--white);font-weight:600;font-size:15px;line-height:1.15;width:150px}
.nav{top:33px;left:0;font-size:12px;font-weight:500;color:var(--white);letter-spacing:.5px}
.nav span{position:absolute;white-space:nowrap}
.nav .active{color:var(--yellow)}
.nav .active::after{content:"";position:absolute;left:0;right:0;bottom:-8px;height:2px;background:var(--yellow)}
.nav .phone{color:var(--white)}
.btn-contact{left:1006px;top:22px;width:109px;height:38px;background:var(--yellow);color:var(--white);font-size:11px;font-weight:600;display:flex;align-items:center;justify-content:center}

/* hero */
.hero{top:80px;height:545px;background:var(--brown)}
.hero-photo{left:84px;top:0;width:1116px;height:545px;background:linear-gradient(160deg,#9db1cc 0%,#5e7089 40%,#34404f 75%,#262c35 100%)}
.hero-title{left:216px;top:250px;color:var(--white);font-size:41px;font-weight:300;line-height:50px}
.hero-title b{font-weight:700}
.btn-yellow{background:var(--yellow);color:var(--white);font-size:10px;font-weight:600;display:flex;align-items:center;justify-content:center}
.hero-btn{left:216px;top:378px;width:108px;height:34px}
.social-strip{left:35px;top:433px;display:flex;flex-direction:column;gap:14px}
.social-strip i{display:block;width:12px;height:12px;border-radius:50%;background:var(--white)}

/* about */
.about{top:625px;height:597px;background:var(--brown)}
.about-photo{left:216px;top:80px;width:307px;height:200px;background:linear-gradient(135deg,#d8d4cf,#a7988a 55%,#6b5443)}
.about-title{left:610px;top:100px;width:400px;color:var(--white);font-size:25px;font-weight:600;line-height:31px}
.about-text{left:610px;top:200px;width:370px;color:var(--muted);font-size:11px;line-height:17px}
.about-text p{margin-bottom:12px}
.link-more{font-size:11px;font-weight:600;color:var(--yellow);letter-spacing:.5px}
.about-link{left:610px;top:325px}
.stat{top:415px;display:flex;align-items:center;gap:14px}
.stat svg{width:110px;height:110px}
.stat-label{color:var(--white)}
.stat-label small{display:block;font-size:9px;color:var(--muted)}
.stat-label strong{display:block;font-size:20px;font-weight:600;line-height:26px}
.stat-label span{display:block;font-size:9px;color:var(--muted);line-height:13px;width:110px}

/* services */
.services{top:1222px;height:498px;background:var(--white)}
.section-title{font-size:25px;font-weight:600;color:var(--ink)}
.services-title{left:216px;top:80px}
.view-all{font-size:10px;font-weight:600;color:var(--ink);letter-spacing:.5px}
.services-view{left:927px;top:92px}
.service{top:166px;width:242px;height:242px;padding:22px 0 0 0}
.service.featured{background:var(--yellow);padding:22px 20px 0;color:var(--white);box-shadow:0 10px 20px rgba(0,0,0,.12)}
.service svg{width:44px;height:44px}
.service h3{font-size:16px;font-weight:600;margin:22px 0 12px}
.service p{font-size:11px;line-height:17px;color:var(--grey);width:210px}
.service.featured p{color:var(--white)}
.service .link-more{display:block;margin-top:26px;color:var(--ink);font-size:9px}
.service.featured .link-more{color:var(--white)}

/* civil works */
.civil{top:1720px;height:690px;background:var(--brown)}
.civil-bg{left:0;top:0}
.civil-word{left:40px;top:625px;transform:rotate(-90deg);transform-origin:left top;font-size:92px;font-weight:700;color:#e6e4e2;white-space:nowrap}
.civil-heading{left:216px;top:245px}
.civil-heading h2{font-size:43px;font-weight:700;color:var(--yellow);line-height:46px}
.civil-heading h3{font-size:25px;font-weight:600;color:var(--ink);margin-top:26px;line-height:30px}
.civil-heading h3 span{display:block;font-size:17px}
.work{color:var(--white)}
.work strong{display:block;font-size:12px;font-weight:500}
.work span{display:block;font-size:10px;color:var(--muted);line-height:15px;width:240px;margin-top:6px}
.hex-num{position:absolute;width:44px;text-align:center;font-size:12px;font-weight:600;color:var(--white)}
.dots{left:1103px;top:320px;display:flex;flex-direction:column;gap:10px}
.dots i{display:block;width:10px;height:10px;border-radius:50%;border:2px solid var(--yellow)}
.dots i.on{background:var(--yellow)}

/* gallery */
.gallery-bar{top:2410px;height:105px;background:var(--yellow)}
.gallery-title{left:216px;top:36px}
.tabs{top:44px;font-size:11px;color:var(--ink)}
.tabs span{position:absolute;white-space:nowrap}
.tab-all{left:690px;top:-6px;width:60px;height:26px;background:var(--brown);color:var(--white);display:flex;align-items:center;justify-content:center;clip-path:polygon(12% 0,100% 0,88% 100%,0 100%)}
.gallery{top:2515px;height:548px}
.tile{position:absolute}
.tile-caption{color:var(--white);text-align:center}
.tile-caption strong{display:block;font-size:15px;font-weight:600;margin-top:12px}
.tile-caption span{font-size:10px;color:var(--muted)}

/* partners */
.partners{top:3063px;height:437px;background:var(--paper)}
.partners-title{left:0;width:1200px;top:85px;text-align:center;font-size:15px;font-weight:600}
.partner{width:160px;height:60px;display:flex;align-items:center;justify-content:center;font-size:24px;font-weight:600;color:#8d8d8d}
.partner.hover{background:var(--white);box-shadow:0 6px 18px rgba(0,0,0,.1);color:#d8262f}
.btn-outline{left:540px;top:323px;width:123px;height:32px;border:1px solid var(--ink);background:var(--white);font-size:10px;font-weight:600;display:flex;align-items:center;justify-content:center}

/* career */
.career{top:3500px;height:365px;background:var(--yellow);overflow:hidden}
.career-photo{left:0;top:0;width:1200px;height:365px;background:linear-gradient(120deg,#c6d5e2 0%,#9db2c4 35%,#d9b27a 70%,#8f6a3e 100%);clip-path:polygon(736px 0,1200px 0,1200px 365px,604px 365px)}
.career-title{left:216px;top:70px;font-size:27px;line-height:34px;color:var(--brown);font-weight:400}
.career-title b{color:var(--white);font-weight:600}
.career-text{left:216px;top:196px;font-size:11px;color:var(--white)}
.btn-dark-outline{left:216px;top:243px;width:126px;height:32px;border:1px solid var(--brown);font-size:10px;font-weight:600;color:var(--brown);display:flex;align-items:center;justify-content:center}

/* footer */
.site-footer{top:3865px;height:350px;background:var(--brown);color:var(--white)}
.footer-brand{left:84px;top:95px;display:flex;align-items:center;gap:14px}
.footer-brand .brand-mark{width:44px;height:44px}
.footer-brand .brand-name{font-size:22px;width:240px;line-height:26px}
.fcol h4{font-size:13px;font-weight:600;margin-bottom:14px}
.fcol p,.fcol li{font-size:11px;color:var(--muted);line-height:19px;list-style:none}
.fcol .call{color:var(--white);font-size:13px}
.sub-input{width:244px;height:30px;background:var(--brown-line);margin-top:16px;display:flex;align-items:center;justify-content:space-between;padding:0 0 0 12px;font-size:10px;color:var(--grey)}
.sub-input i{width:30px;height:30px;background:var(--yellow);display:flex;align-items:center;justify-content:center}
.copyright{left:0;top:295px;width:1200px;height:55px;border-top:1px solid var(--brown-line)}
.copyright p{position:absolute;left:84px;top:20px;font-size:10px;color:var(--muted)}
.copyright b{color:var(--yellow);font-weight:500}
.foot-social{right:84px;top:14px;display:flex;gap:8px}
.foot-social i{display:block;width:24px;height:24px;border-radius:50%;border:1px solid var(--yellow)}
.foot-social i.on{background:var(--yellow)}
</style>
</head>
<body>

<header class="site-header">
  <div class="abs brand"><span class="brand-mark"></span><span class="brand-name">Cobaltrine Building Company</span></div>
  <nav class="abs nav">
    <span class="active" style="left:427px">HOME</span>
    <span style="left:486px">ABOUT</span>
    <span style="left:551px">DIVISIONS</span>
    <span style="left:638px">GALLERY</span>
    <span style="left:714px">SUPPLIES</span>
    <span style="left:798px">CAREER</span>
    <span class="phone" style="left:863px">&#9742; +966 12 555 0147</span>
  </nav>
  <div class="abs btn-contact">CONTACT US</div>
</header>

<section class="hero">
  <div class="abs hero-photo" role="img" aria-label="Glass high-rise towers and tower cranes against a blue sky"></div>
  <h1 class="abs hero-title"><b>Cobaltrine</b> is a Innovation<br>Construction</h1>
  <div class="abs btn-yellow hero-btn">EXPLORE MORE</div>
  <div class="abs social-strip"><i></i><i></i><i></i><i></i></div>
</section>

<section class="about">
  <div class="abs about-photo" role="img" aria-label="Finished modern living room interior with fireplace and sofa"></div>
  <h2 class="abs about-title">We Specialized in waterproofing &amp; specialized finishing,</h2>
  <div class="abs about-text">
    <p>With the main target of furnishing the Saudi market by a professional team of engineers and applicators to abide by the need of the fast growing construction world in the Kingdom.</p>
    <p>In 2005, since the company's humble beginning commitment to deliver the highest quality work on schedule and within budget.</p>
  </div>
  <div class="abs link-more about-link">DISCOVER MORE &#8250;</div>

  <div class="abs stat" style="left:212px">
    <svg viewBox="0 0 110 110"><circle cx="55" cy="55" r="50" fill="none" stroke="var(--brown-line)" stroke-width="3"/><circle cx="55" cy="55" r="50" fill="none" stroke="var(--yellow)" stroke-width="3" stroke-dasharray="110 314" transform="rotate(-90 55 55)"/><text x="55" y="64" text-anchor="middle" font-family="Poppins,sans-serif" font-size="26" fill="var(--yellow)">35%</text></svg>
    <div class="stat-label"><small>Projects</small><strong>Codes</strong><span>Lorem ipsum dolor sit amet message</span></div>
  </div>
  <div class="abs stat" style="left:473px">
    <svg viewBox="0 0 110 110"><circle cx="55" cy="55" r="50" fill="none" stroke="var(--brown-line)" stroke-width="3"/><circle cx="55" cy="55" r="50" fill="none" stroke="var(--yellow)" stroke-width="3" stroke-dasharray="236 314" transform="rotate(-90 55 55)"/><text x="55" y="64" text-anchor="middle" font-family="Poppins,sans-serif" font-size="26" fill="var(--yellow)">75%</text></svg>
    <div class="stat-label"><small>Happy</small><strong>Clients</strong><span>Lorem ipsum dolor sit amet message</span></div>
  </div>
  <div class="abs stat" style="left:740px">
    <svg viewBox="0 0 110 110"><circle cx="55" cy="55" r="50" fill="none" stroke="var(--brown-line)" stroke-width="3"/><circle cx="55" cy="55" r="50" fill="none" stroke="var(--yellow)" stroke-width="3" stroke-dasharray="214 314" transform="rotate(-90 55 55)"/><text x="55" y="64" text-anchor="middle" font-family="Poppins,sans-serif" font-size="26" fill="var(--yellow)">68%</text></svg>
    <div class="stat-label"><small>Completed</small><strong>Projects</strong><span>Lorem ipsum dolor sit amet message</span></div>
  </div>
</section>

<section class="services">
  <h2 class="abs section-title services-title">Our Services</h2>
  <div class="abs view-all services-view">VIEW ALL &#8250;</div>

  <article class="abs service" style="left:216px">
    <svg viewBox="0 0 44 44" fill="none" stroke="var(--yellow)" stroke-width="2"><path d="M6 22 22 8l16 14"/><path d="M10 19v18h24V19"/><rect x="18" y="26" width="8" height="11"/></svg>
    <h3>Residential</h3>
    <p>Contrary to popular belief, Lorem Ipsum is not simply random text. It has roots in a piece of classical Latin literature from 45 BC, making it over...</p>
    <span class="link-more">READ MORE &#8250;</span>
  </article>
  <article class="abs service" style="left:479px">
    <svg viewBox="0 0 44 44" fill="none" stroke="var(--yellow)" stroke-width="2"><rect x="8" y="14" width="12" height="24"/><rect x="22" y="6" width="14" height="32"/><path d="M12 20h4M12 26h4M26 12h6M26 18h6M26 24h6"/></svg>
    <h3>Commercial</h3>
    <p>Contrary to popular belief, Lorem Ipsum is not simply random text. It has roots in a piece of classical Latin literature from 45 BC, making it over...</p>
    <span class="link-more">READ MORE &#8250;</span>
  </article>
  <article class="abs service featured" style="left:742px;top:166px">
    <svg viewBox="0 0 44 44" fill="none" stroke="var(--white)" stroke-width="2"><path d="M6 38V20l10 6v-6l10 6V10h8v28z"/><path d="M28 6h4"/></svg>
    <h3>Industrial</h3>
    <p>Contrary to popular belief, Lorem Ipsum is not simply random text. It has roots in a piece of classical Latin literature from 45 BC, making it over...</p>
    <span class="link-more">READ MORE &#8250;</span>
  </article>
</section>

<section class="civil">
  <svg class="abs civil-bg" width="1200" height="690" viewBox="0 0 1200 690">
    <polygon points="0,0 267,0 604,345 267,690 0,690" fill="var(--paper)"/>
    <g stroke="var(--brown-line)" stroke-width="1">
      <line x1="340" y1="81" x2="860" y2="81"/><line x1="432" y1="171" x2="930" y2="171"/>
      <line x1="528" y1="258" x2="990" y2="258"/><line x1="621" y1="345" x2="1050" y2="345"/>
      <line x1="528" y1="432" x2="990" y2="432"/><line x1="432" y1="520" x2="930" y2="520"/>
      <line x1="340" y1="607" x2="860" y2="607"/>
    </g>
    <g stroke="var(--yellow)" stroke-width="2" fill="var(--brown)">
      <polygon points="318,59 337,70 337,92 318,103 299,92 299,70"/>
      <polygon points="410,149 429,160 429,182 410,193 391,182 391,160"/>
      <polygon points="506,236 525,247 525,269 506,280 487,269 487,247" fill="var(--yellow)"/>
      <polygon points="599,323 618,334 618,356 599,367 580,356 580,334"/>
      <polygon points="506,410 525,421 525,443 506,454 487,443 487,421"/>
      <polygon points="410,498 429,509 429,531 410,542 391,531 391,509"/>
      <polygon points="318,585 337,596 337,618 318,629 299,618 299,596"/>
    </g>
  </svg>
  <div class="civil-word abs">Civil Works</div>
  <div class="abs civil-heading">
    <h2>General<br>Activity</h2>
    <h3>Specialized<span>Activity</span></h3>
  </div>

  <span class="hex-num" style="left:296px;top:72px">01</span>
  <span class="hex-num" style="left:388px;top:162px">02</span>
  <span class="hex-num" style="left:484px;top:249px">03</span>
  <span class="hex-num" style="left:577px;top:336px">04</span>
  <span class="hex-num" style="left:484px;top:423px">05</span>
  <span class="hex-num" style="left:388px;top:511px">06</span>
  <span class="hex-num" style="left:296px;top:598px">07</span>

  <div class="abs work" style="left:543px;top:60px"><strong>General Contracting</strong><span>Lorem ipsum dolor sit amet message Contrary to popular belief. Lorem</span></div>
  <div class="abs work" style="left:610px;top:150px"><strong>Environmental Works</strong><span>Lorem ipsum dolor sit amet message Contrary to popular belief. Lorem</span></div>
  <div class="abs work" style="left:675px;top:237px"><strong>Marine Works</strong><span>Lorem ipsum dolor sit amet message Contrary to popular belief. Lorem</span></div>
  <div class="abs work" style="left:742px;top:324px"><strong>Landscape Works</strong><span>Lorem ipsum dolor sit amet message Contrary to popular belief. Lorem</span></div>
  <div class="abs work" style="left:675px;top:411px"><strong>Steel Works</strong><span>Lorem ipsum dolor sit amet message Contrary to popular belief. Lorem</span></div>
  <div class="abs work" style="left:610px;top:499px"><strong>Finishing Works</strong><span>Lorem ipsum dolor sit amet message Contrary to popular belief. Lorem</span></div>
  <div class="abs work" style="left:543px;top:586px"><strong>Concrete Works</strong><span>Lorem ipsum dolor sit amet message Contrary</span></div>

  <div class="abs dots"><i class="on"></i><i></i><i></i></div>
</section>

<section class="gallery-bar">
  <h2 class="abs section-title gallery-title">Projects Gallery</h2>
  <div class="abs tabs" style="left:0;width:1200px">
    <span class="tab-all">All</span>
    <span style="left:775px">Residential</span>
    <span style="left:862px">Commercial</span>
    <span style="left:945px">Industrial</span>
  </div>
</section>

<section class="gallery">
  <div class="tile" style="left:0;top:0;width:590px;height:275px;background:linear-gradient(180deg,#8fb6dc,#c7d8e6 60%,#8b8070)" role="img" aria-label="Tower cranes above a concrete building under construction"></div>
  <div class="tile" style="left:590px;top:0;width:304px;height:275px;background:#3f342b;display:flex;align-items:center;justify-content:center">
    <div class="tile-caption"><svg width="40" height="40" viewBox="0 0 40 40"><rect width="40" height="40" fill="var(--yellow)"/></svg><strong>Construction Build</strong><span>Contrary to popular</span></div>
  </div>
  <div class="tile" style="left:894px;top:0;width:306px;height:275px;background:linear-gradient(160deg,#a8c4dc,#d6c7a2 60%,#7c6a55)" role="img" aria-label="Workers on steel scaffolding at a building site"></div>
  <div class="tile" style="left:0;top:275px;width:304px;height:273px;background:linear-gradient(180deg,#e7b873,#a3683a 60%,#3c2a1d)" role="img" aria-label="Silhouetted builders on a frame at sunset"></div>
  <div class="tile" style="left:304px;top:275px;width:306px;height:273px;background:linear-gradient(180deg,#7aa6d6,#b5c6d4 55%,#c39a4e)" role="img" aria-label="Yellow excavator working on a site"></div>
  <div class="tile" style="left:610px;top:275px;width:590px;height:273px;background:linear-gradient(170deg,#d9d6cf,#b9aa92 55%,#6e5b46)" role="img" aria-label="Workers in hard hats tying rebar on a concrete deck"></div>
</section>

<section class="partners">
  <h2 class="abs partners-title">Partners and Affiliates</h2>
  <div class="abs partner" style="left:229px;top:142px">Norvix</div>
  <div class="abs partner hover" style="left:406px;top:142px">Tellora</div>
  <div class="abs partner" style="left:617px;top:142px">Linkara</div>
  <div class="abs partner" style="left:819px;top:142px">Wavesta</div>
  <div class="abs partner" style="left:229px;top:220px">Datafold</div>
  <div class="abs partner" style="left:406px;top:220px">Hartwell</div>
  <div class="abs partner" style="left:617px;top:220px">Lumora</div>
  <div class="abs partner" style="left:819px;top:220px">Voxline</div>
  <div class="abs btn-outline">VIEW ALL</div>
</section>

<section class="career">
  <div class="abs career-photo" role="img" aria-label="Smiling construction workers in hard hats on site"></div>
  <h2 class="abs career-title">If you find a Lorem Ipsum<br><b>Secure Job</b> For Your<br>Carrier?</h2>
  <p class="abs career-text">Contrary to popular belief, Lorem Ipsum</p>
  <div class="abs btn-dark-outline">FIND YOUR JOB</div>
</section>

<footer class="site-footer">
  <div class="abs footer-brand"><span class="brand-mark"></span><span class="brand-name">Cobaltrine Building Company</span></div>
  <div class="abs fcol" style="left:433px;top:80px;width:220px">
    <h4>Contact Us</h4>
    <p class="call">Call &nbsp; +966 12 555 0147</p>
    <p>E &nbsp; info@cobaltrine.com</p>
    <p style="color:var(--white);margin-top:4px">Address:</p>
    <p>Jeddah - Palm Street - Al<br>Rawdah</p>
  </div>
  <div class="abs fcol" style="left:697px;top:80px">
    <h4>Quick Links</h4>
    <ul><li>About</li><li>Divisions</li><li>Gallery</li><li>Supplies</li><li>Career</li><li>Contact</li></ul>
  </div>
  <div class="abs fcol" style="left:874px;top:80px">
    <h4>Subscribe Now!</h4>
    <p>Your Mail to get Update<br>about Upcoming News? Join Us Now!</p>
    <div class="sub-input">Enter Your Email<i><svg width="10" height="10" viewBox="0 0 10 10"><path d="M2 1l5 4-5 4" fill="none" stroke="#fff" stroke-width="1.6"/></svg></i></div>
  </div>
  <div class="abs copyright">
    <p>&copy; 2019 <b>Cobaltrine Building Company</b>. All Right Reserved</p>
    <div class="abs foot-social"><i></i><i class="on"></i><i></i><i></i></div>
  </div>
</footer>

</body>
</html>
```